Paper Lantern Theory - Podcast Cover

Paper Lantern Theory is a weekly podcast that dispels some of the myths about conventional economic thinking and provides a new way of thinking about issues that are faced by the global economy. It's insightful, thought-provoking and, most importantly, fun. We are refreshing the look and sound of the podcast. I have attached a copy of the old amateur design (which I did!)

Target Market(s)

Male oriented, smart folk with an interest in politics and economics

Font styles to use
Sans Serif

Requirements
Must have
• Clearly visible title, even when reduced in size. Must be 3000 pixels by 3000 pixels.
Nice to have
• This podcast challenges the status quo. It should reflect that. Photos and names of the hosts. Actually, because th ephotos are so different, we'd be open to the idea of a caricature if you can do that within the price.

```html
<!DOCTYPE html>
<html lang="en">
<head>
<meta charset="utf-8">
<title>Paper Lantern Theory – Podcast Cover</title>
<link href="https://fonts.googleapis.com/css2?family=Archivo+Black&family=Montserrat:wght@700;800&display=swap" rel="stylesheet">
<style>
  :root{
    --stage:#ebe8e4;
    --paper:#ffffff;
    --ink:#161616;
    --red:#c8161d;
    --money-light:#eef0ea;
    --money-mid:#b9c2b2;
    --money-dark:#7d8a78;
    --skin-a:#d9b8a0;
    --skin-b:#8aa5b8;
  }
  *{margin:0;padding:0;box-sizing:border-box}
  html,body{width:1200px;height:807px;overflow:hidden;background:var(--stage)}
  .cover{
    position:absolute;left:240px;top:43px;width:720px;height:720px;
    background:var(--paper);overflow:hidden;
    font-family:"Archivo Black",sans-serif;color:var(--ink);
  }
  .mic-icon{position:absolute;left:32px;top:30px;width:58px;height:58px}
  .hero-art{
    position:absolute;left:300px;top:22px;width:330px;height:368px;
    background:radial-gradient(ellipse at 50% 45%,var(--money-light) 0%,var(--money-mid) 55%,var(--paper) 78%);
    border-radius:40% 40% 30% 30%;
  }
  .hero-art .drain{position:absolute;left:125px;bottom:6px;width:80px;height:22px;border-radius:50%;background:var(--money-dark)}
  .title{position:absolute;left:0;top:388px;width:720px;text-transform:uppercase;line-height:60px;letter-spacing:-1px}
  .title span{display:block;font-size:68px}
  .title .the{padding-left:96px}
  .title .name-red{padding-left:38px;color:var(--red);font-size:64px}
  .title .name-dark{padding-left:96px}
  .label-rule{position:absolute;left:50px;top:578px;width:620px;height:20px;display:flex;align-items:center;gap:14px}
  .label-rule::before,.label-rule::after{content:"";flex:1;height:3px;background:var(--ink)}
  .label-rule span{font-family:"Montserrat",sans-serif;font-weight:800;font-size:17px;letter-spacing:3px}
  .hosts{position:absolute;left:0;top:620px;width:720px;height:100px}
  .hosts .band{position:absolute;left:128px;top:36px;width:472px;height:40px;background:var(--red);display:flex}
  .hosts .band span{flex:1;display:flex;align-items:center;justify-content:center;color:#fff;font-family:"Montserrat",sans-serif;font-weight:800;font-size:19px;letter-spacing:.5px}
  .hosts .band span+span{border-left:3px solid #fff;flex:1.25}
  .portrait{position:absolute;top:6px;width:98px;height:98px;border-radius:50%;border:3px solid #fff}
  .portrait.left{left:38px;background:linear-gradient(160deg,var(--skin-a),var(--skin-b))}
  .portrait.right{left:590px;background:linear-gradient(160deg,#5b5b5b,var(--skin-a) 60%,#f2f2f2)}
</style>
</head>
<body>
  <main class="cover">
    <svg class="mic-icon" viewBox="0 0 60 60" aria-hidden="true" fill="none" stroke="var(--ink)" stroke-width="4" stroke-linecap="round">
      <rect x="22" y="6" width="16" height="28" rx="8" fill="var(--ink)"/>
      <path d="M15 24a15 15 0 0 0 30 0"/>
      <path d="M30 39v10M21 52h18"/>
      <path d="M9 14a24 24 0 0 0 0 22M51 14a24 24 0 0 1 0 22"/>
    </svg>

    <div class="hero-art" role="img" aria-label="Dollar bills swirling up out of a drain">
      <div class="drain"></div>
    </div>

    <h1 class="title">
      <span class="the">The</span>
      <span class="name-red">Paper Lantern</span>
      <span class="name-dark">Theory</span>
    </h1>

    <div class="label-rule"><span>PODCAST</span></div>

    <div class="hosts">
      <div class="band"><span>NED ARBURY</span><span>PROF. MILES CORRAN</span></div>
      <div class="portrait left" role="img" aria-label="Portrait photo of host Ned Arbury"></div>
      <div class="portrait right" role="img" aria-label="Portrait photo of host Prof. Miles Corran"></div>
    </div>
  </main>
</body>
</html>
```